B2B EDM Banner Design- Specialist Tech Company

We need a new top-of-email banner for our EDM campaigns for Varnel Brix (www.varnelbrix-example.com
). This banner will sit at the top of every email and must immediately signal the brand, look modern and professional, and be visually aligned with the tech/IT audience.
Size of the banner: Around 728x90 - it must fit at the top of an email blast.
Purpose of the Banner
Establish a strong, recognizable brand identity across all Varnel Brix EDMs
visually consistent with existing banners created for other brands (see reference examples provided)
Communicate Varnel Brix’s value proposition at a glance
Brand Name
Varnel Brix
Tagline (must appear in the banner)
“11,322 whitepapers from 726 companies”
Design Requirements
Style & Tone
Modern, clean, and professional
Tech-centric look and feel
High-quality, sleek, and corporate
Eye-catching but not cluttered
Should feel premium and authoritative
Layout & Composition
Full-width banner for email header
Horizontal orientation similar to the Plomtar and Quindle Staff Archive examples
Include space for the brand name/logo prominently on the left or centered
Integrate the tagline in a readable, secondary position
Optional: a subtle background texture or tech-related abstract pattern (circuitry, network nodes, gradient, etc.)
No busy imagery—should feel clean and trustworthy
Color Palette
Use colors consistent with Varnel Brix branding from www.varnelbrix-example.com
Blues, greys, blacks, and tech-style gradients preferred
Should feel consistent with a B2B IT audience
Typography
Clean, sans-serif fonts (professional/tech-aligned)
Brand name should be bold and prominent
Tagline should be smaller, but still readable on desktop and mobile
Imagery (if used)
Abstract tech shapes, network visuals, geometric patterns, or gradient overlays
Avoid photography of people
Keep imagery subtle so text remains legible
Call-to-Action Button (optional)
None required in this banner (unlike the HR examples)
Banner should remain a pure brand header
Deliverables
Final banner in PNG and JPG formats
2–3 design variations (if possible) for A/B testing
Dimensions optimized for EDM: ~600–700px wide (standard email width), proportionate height

```html
<!DOCTYPE html>
<html lang="en">
<head>
<meta charset="utf-8">
<title>Varnel Brix – Email Header Banner</title>
<link rel="stylesheet" href="https://fonts.googleapis.com/css2?family=Montserrat:wght@400;600;800&display=swap">
<style>
  :root {
    --navy-deep: #08162c;
    --navy: #0f2a4d;
    --navy-edge: #1a3d66;
    --graphite: #343538;
    --graphite-light: #404144;
    --circuit-blue: #1f7fb8;
    --accent-blue: #2ba3df;
    --white: #ffffff;
    --soft-white: #e4e7eb;
  }

  html, body {
    margin: 0;
    padding: 0;
    overflow: hidden;
    background: var(--graphite);
  }

  .banner {
    position: relative;
    width: 1200px;
    height: 148px;
    overflow: hidden;
    background: linear-gradient(90deg, var(--graphite) 0%, var(--graphite-light) 60%, var(--graphite) 100%);
    font-family: "Montserrat", Arial, sans-serif;
  }

  .circuit-field {
    position: absolute;
    inset: 0 0 0 500px;
    background:
      radial-gradient(ellipse 55% 35% at 70% 0%, rgba(31,127,184,0.45), transparent 70%),
      radial-gradient(ellipse 50% 35% at 55% 100%, rgba(31,127,184,0.5), transparent 70%),
      radial-gradient(ellipse 25% 30% at 8% 100%, rgba(31,127,184,0.35), transparent 70%);
  }

  .brand-panel {
    position: absolute;
    left: 0;
    top: 0;
    width: 560px;
    height: 148px;
    filter: drop-shadow(6px 0 10px rgba(0,0,0,0.45));
  }

  .brand {
    position: absolute;
    left: 110px;
    top: 44px;
    display: flex;
    align-items: center;
    gap: 16px;
  }

  .brand-mark {
    width: 64px;
    height: 64px;
    border-radius: 50%;
    background: var(--accent-blue);
    flex: none;
  }

  .brand-text {
    display: flex;
    flex-direction: column;
  }

  .brand-name {
    margin: 0;
    color: var(--white);
    font-weight: 800;
    font-size: 33px;
    line-height: 1;
    letter-spacing: 0.5px;
    text-transform: uppercase;
  }

  .brand-subline {
    margin: 8px 0 0;
    color: var(--accent-blue);
    font-weight: 600;
    font-size: 11.5px;
    line-height: 1;
    letter-spacing: 2.6px;
    text-transform: uppercase;
  }

  .tagline {
    position: absolute;
    left: 628px;
    top: 60px;
    margin: 0;
    color: var(--soft-white);
    font-weight: 400;
    font-size: 20px;
    line-height: 1.2;
    letter-spacing: 1.4px;
    white-space: nowrap;
  }

  .tagline .figure {
    color: var(--accent-blue);
    font-weight: 800;
  }
</style>
</head>
<body>
  <header class="banner">
    <div class="circuit-field" role="img" aria-label="Abstract blue circuit-board lines glowing along the top and bottom edges"></div>

    <svg class="brand-panel" viewBox="0 0 560 148" role="img" aria-label="Dark navy panel with a faint hexagon texture, ending in a pointed chevron">
      <defs>
        <linearGradient id="panelFill" x1="0" y1="0" x2="1" y2="0">
          <stop offset="0" stop-color="#08162c"/>
          <stop offset="0.7" stop-color="#0d2443"/>
          <stop offset="1" stop-color="#12325a"/>
        </linearGradient>
        <linearGradient id="edgeFill" x1="0" y1="0" x2="1" y2="0">
          <stop offset="0" stop-color="#12325a"/>
          <stop offset="1" stop-color="#1e4672"/>
        </linearGradient>
      </defs>
      <polygon points="0,0 502,0 540,74 502,148 0,148" fill="url(#edgeFill)"/>
      <polygon points="0,0 494,0 532,74 494,148 0,148" fill="url(#panelFill)"/>
    </svg>

    <div class="brand">
      <span class="brand-mark" aria-hidden="true"></span>
      <div class="brand-text">
        <h1 class="brand-name">Varnel Brix</h1>
        <p class="brand-subline">For IT Professionals</p>
      </div>
    </div>

    <p class="tagline"><span class="figure">11322</span> Whitepapers from <span class="figure">726</span> Companies</p>
  </header>
</body>
</html>
```